【 概要 】 ホームページのTOP画像のデザインを募集いたします。 飲食店専用ホームページ制作です。 メインターゲットは飲食店オーナーの方々です。 飲食のホームページにあった「どんなお店なのか」、「どんなメニュ・どんなコースがあるか」など、 そのお店を気になった方々に来店を促すようなTOP画像が希望です。 【 依頼内容 】 ・サイズ:1920px×1080px ・作成数: 1種類 ・利用用途:ホームページトップ画像 ・色:オレンジ/赤/黄色 ・文言:あなたのお店をオリジナルデザインで作ってみませんか? 【 デザインイメージ 】 ・雰囲気:信頼感、安心感があり、ポップ感 ・現在制作途中のホームページにあった感じ http://sampwebnoren.com/ ・参考他社デザイン https://www.hanamuraya.co.jp/menu/kikaku/ また飲食以外も対象にしたいと思ったので別案も制作していただけたら幸いです。 【 依頼内容 】 色:グレー/白/黒 文言:ホームページはオリジナルデザインで! 参考URL:https://qv-webworks.jp/hp/?utm_source=kensaku&utm_medium=cpc&qclid=QRS.2004815367.PXbTwLcdFhZNruqk5p8w27AKRGetSd3hvm-qWFBCZjBXFgKQ5_E_CzX 【 契約金額(税抜) 】 1万円 ※契約金額(税込)からシステム利用料を差し引いた金額が、ワーカーさまの受取金額となります その他ご質問等ありましたら、気軽にお問い合わせください。 ご応募をお待ちしております! |
| https://www.hanamuraya.co.jp/menu/kikaku/ | ||
私共の内容をよく理解していただいた上で作成していただきありがとうございます。
今回korunote様のご提案が弊社のHPの表画面での使用に一番最適だと考え作用させていただきます。
皆様色々ご提案ありがとうございます。とても素敵なデザインを見していただきました。
弊社は今後よくご依頼などをさせていただきますので、その際は皆様また力を貸していただければと思います。

```html
<!DOCTYPE html>
<html lang="ja">
<head>
<meta charset="UTF-8">
<title>あなたのお店のオリジナルデザイン</title>
<link rel="stylesheet" href="https://fonts.googleapis.com/css2?family=M+PLUS+Rounded+1c:wght@500;800&display=swap">
<style>
  :root {
    --coral: #f2545b;
    --pin-yellow: #fcd84c;
    --icon-orange: #f58a3c;
    --text-dark: #3a2a24;
    --text-white: #ffffff;
    --title-outline: #f47a35;
    --interior-a: #7a3b4a;
    --interior-b: #c2596a;
    --kitchen-a: #b8566a;
    --kitchen-b: #e89aa4;
  }
  html, body {
    margin: 0;
    padding: 0;
    overflow: hidden;
    background: #ffffff;
  }
  .hero {
    position: relative;
    width: 1200px;
    height: 676px;
    overflow: hidden;
    font-family: "M PLUS Rounded 1c", sans-serif;
  }
  .photo {
    position: absolute;
  }
  .photo--interior {
    left: 0;
    top: 0;
    width: 840px;
    height: 676px;
    background: linear-gradient(135deg, var(--interior-a) 0%, var(--interior-b) 55%, #9c4a58 100%);
  }
  .photo--kitchen {
    left: 820px;
    top: 190px;
    width: 380px;
    height: 486px;
    background: linear-gradient(160deg, var(--kitchen-b) 0%, var(--kitchen-a) 60%, #8c3f50 100%);
  }
  .band {
    position: absolute;
    background: var(--coral);
  }
  .band--top-right {
    left: 710px;
    top: 0;
    width: 490px;
    height: 190px;
  }
  .band--bottom-left {
    left: 0;
    top: 600px;
    width: 540px;
    height: 76px;
  }
  .pin {
    position: absolute;
    left: 0;
    top: 0;
    width: 1200px;
    height: 676px;
  }
  .copy {
    position: absolute;
    left: 0;
    width: 1200px;
    text-align: center;
    margin: 0;
  }
  .copy__lead {
    top: 382px;
    font-size: 30px;
    font-weight: 500;
    color: var(--text-dark);
    letter-spacing: 2px;
  }
  .copy__title {
    top: 440px;
    font-size: 64px;
    font-weight: 800;
    color: var(--text-white);
    letter-spacing: 3px;
    -webkit-text-stroke: 3px var(--title-outline);
    paint-order: stroke fill;
    text-shadow: 0 3px 0 var(--title-outline);
  }
  .copy__tail {
    top: 560px;
    font-size: 30px;
    font-weight: 500;
    color: var(--text-dark);
    letter-spacing: 2px;
  }
</style>
</head>
<body>
  <main class="hero">
    <div class="photo photo--interior" role="img" aria-label="テーブルが並ぶレストランの店内写真"></div>
    <div class="photo photo--kitchen" role="img" aria-label="フライパンで料理を調理する手元の写真"></div>
    <div class="band band--top-right"></div>
    <div class="band band--bottom-left"></div>

    <svg class="pin" viewBox="0 0 1200 676" aria-hidden="true">
      <path fill="var(--pin-yellow)" d="M600,676 C540,600 320,480 320,292 A280,280 0 1 1 880,292 C880,480 660,600 600,676 Z"/>
      <g fill="var(--icon-orange)">
        <!-- fork -->
        <rect x="498" y="92" width="14" height="92" rx="7"/>
        <rect x="528" y="92" width="14" height="92" rx="7"/>
        <rect x="558" y="92" width="14" height="92" rx="7"/>
        <path d="M498,170 H572 V190 Q572,218 546,224 V318 Q546,330 535,330 Q524,330 524,318 V224 Q498,218 498,190 Z"/>
        <!-- knife -->
        <path d="M650,90 Q700,110 702,200 L702,230 H676 V318 Q676,330 665,330 Q654,330 654,318 Z"/>
      </g>
    </svg>

    <p class="copy copy__lead">あなたのお店の</p>
    <h1 class="copy copy__title">オリジナルデザイン</h1>
    <p class="copy copy__tail">で作ってみませんか？</p>
  </main>
</body>
</html>
```